Golden Meadow Kit Social Media Graphics

Focusing on the Golden Meadow Kit product (3 product bundle), create 6-7 individual social media graphics (square size). For the color scheme of the graphics, they should all be complementary with the Golden Meadow Kit bottle colors.

Note: each graphic should have one of the pictures of the bottles (3-product bundle) on it and/or one of the images with a person on it (several pics attached to choose from). I even included some real customer “before and afters” pictures…you can use them if you think the quality is good enough.

Target Market(s)

men and women looking for fast, healthy loss

Industry/Entity Type

health and wellness

Requirements
Must have
• the product is a picture of ALL 3 bottles; no single bottles will be selected

```html
<!DOCTYPE html>
<html lang="en">
<head>
<meta charset="utf-8">
<title>Golden Meadow Kit Social Media Graphics</title>
<link href="https://fonts.googleapis.com/css2?family=Montserrat:wght@400;500;600;700;800&display=swap" rel="stylesheet">
<style>
:root{
  --board:#7b7b7b;
  --white:#ffffff;
  --navy:#26307a;
  --royal:#2b3fa3;
  --bright-blue:#2f4fc9;
  --red:#e11f2d;
  --plum:#4f2448;
  --orchid:#c27bad;
  --mist:#dcdde3;
  --ink:#141414;
}
*{margin:0;padding:0;box-sizing:border-box}
html,body{width:1200px;height:809px;overflow:hidden;background:var(--board);font-family:'Montserrat',sans-serif}
.board{position:relative;width:1200px;height:809px}
.post{position:absolute;width:379px;height:379px;overflow:hidden}
.post > *{position:absolute}
.bottles{border-radius:10px;background:linear-gradient(180deg,#f7f8fa,#d9dce6 70%,#c9a0c4)}
.eyebrow{font-weight:500;text-transform:uppercase;letter-spacing:.2px}
.headline{font-weight:800;text-transform:uppercase;line-height:1.12}
.benefits{list-style:none}
.benefits li{display:flex;align-items:center;gap:3px;font-weight:500;white-space:nowrap}
.benefits svg{width:7px;height:7px;flex:none}
.icon{border-radius:50%}
.icon-label{text-align:center;font-weight:500;line-height:1.25}

/* 1 */
.post-solution{left:17px;top:12px;background:var(--white)}
.post-solution .photo{left:0;top:0;width:379px;height:270px;background:linear-gradient(90deg,#8a6a55,#c8b6a6 45%,#6e5546 60%,#d9cfc6)}
.post-solution .wave{left:0;top:190px;width:379px;height:189px}
.post-solution .eyebrow{left:18px;top:236px;font-size:7.6px;color:var(--ink)}
.post-solution .headline{left:18px;top:250px;font-size:15.4px;color:var(--royal);line-height:1.2}
.post-solution .benefits{left:20px;top:302px;font-size:7.3px;color:var(--navy)}
.post-solution .benefits li{height:14.4px}
.post-solution .bottles{left:213px;top:221px;width:147px;height:136px}

/* 2 */
.post-struggle{left:411px;top:12px;background:var(--white)}
.post-struggle .photo{left:0;top:0;width:379px;height:226px;background:linear-gradient(180deg,#f3f4f6,#d6a98a 55%,#efefef)}
.post-struggle .tag{left:79px;top:211px;width:221px;height:29px;background:var(--red);border-radius:9px 9px 0 0;color:var(--white);font-weight:700;font-size:10.6px;display:flex;align-items:center;justify-content:center}
.post-struggle .headline{left:0;top:254px;width:379px;text-align:center;font-size:14.8px;color:var(--ink)}
.post-struggle .frame{left:38px;top:285px;width:302px;height:54px;border:1px solid var(--red)}
.post-struggle .benefits{left:51px;top:297px;width:290px;display:grid;grid-template-columns:131px 159px;row-gap:8px;font-size:7.6px;color:var(--ink)}

/* 3 */
.post-natural{left:804px;top:12px;background:var(--plum)}
.post-natural .eyebrow{left:0;top:35px;width:379px;text-align:center;font-size:9.4px;color:var(--white)}
.post-natural .headline{left:0;top:50px;width:379px;text-align:center;font-size:16.6px;color:var(--white);line-height:1.25}
.post-natural .panel{left:190px;top:140px;width:189px;height:239px;background:var(--orchid)}
.post-natural .photo{left:20px;top:114px;width:195px;height:246px;background:linear-gradient(180deg,#8a6a52,#c7a98f 40%,#efe7e2 75%,#d8d2cc)}
.post-natural .icon{left:264px;width:25px;height:25px;background:var(--plum);border:1px solid #7a4273}
.post-natural .icon-label{left:216px;width:121px;font-size:6.6px;color:var(--white)}

/* 4 */
.post-beforeafter{left:17px;top:407px;background:linear-gradient(160deg,#2b3c98,#2447b8 55%,#1f5ad8)}
.post-beforeafter .headline{left:0;top:36px;width:379px;text-align:center;font-size:16.8px;color:var(--white);line-height:1.32}
.post-beforeafter .photo{top:127px;width:158px;height:190px;border-radius:30px 30px 45px 45px}
.post-beforeafter .before{left:26px;background:linear-gradient(180deg,#6b7c5a,#3a3030 50%,#8d8a83)}
.post-beforeafter .after{left:195px;background:linear-gradient(180deg,#b08a55,#d8cde2 50%,#7a3d9e)}
.post-beforeafter .caption{top:322px;width:158px;text-align:center;font-size:11px;font-weight:700;color:var(--white)}
.post-beforeafter .cap-before{left:26px}
.post-beforeafter .cap-after{left:195px}
.post-beforeafter .swoosh{left:0;top:300px;width:379px;height:79px}

/* 5 */
.post-double{left:411px;top:407px;background:var(--mist)}
.post-double .base{left:0;top:0;width:379px;height:379px}
.post-double .photo{left:212px;top:10px;width:160px;height:262px;background:linear-gradient(180deg,#3a2a22,#8a5a3e 30%,#e4e4ea 55%,#2a2a2e)}
.post-double .headline{left:22px;top:47px;font-size:19.2px;color:var(--plum);line-height:1.27}
.post-double .bottles{left:18px;top:178px;width:200px;height:170px}
.post-double .benefits{left:240px;top:292px;font-size:6.6px;color:var(--white)}
.post-double .benefits li{height:14.4px}

/* 6 */
.post-discover{left:806px;top:407px;background:var(--white)}
.post-discover .photo{left:0;top:0;width:379px;height:269px;background:linear-gradient(90deg,#f6f1f1 40%,#efc3cf 65%,#e697ad)}
.post-discover .eyebrow{left:19px;top:53px;font-size:8.4px;color:var(--ink)}
.post-discover .headline{left:19px;top:68px;font-size:19px;color:var(--bright-blue);line-height:1.28}
.post-discover .snap{top:155px;width:86px;height:86px;border-radius:5px}
.post-discover .snap-before{left:19px;background:linear-gradient(180deg,#6f8a5a,#d6b9a8 45%,#2a2a2a)}
.post-discover .snap-after{left:109px;background:linear-gradient(180deg,#7fa36a,#e0bfb3 45%,#4a6fc4)}
.post-discover .bottles{left:17px;top:252px;width:136px;height:113px}
.post-discover .icon{width:23px;height:23px;background:var(--bright-blue)}
.post-discover .icon-label{font-size:6.2px;color:var(--ink)}
</style>
</head>
<body>
<svg width="0" height="0" style="position:absolute">
  <defs>
    <symbol id="bullet" viewBox="0 0 10 10">
      <circle cx="5" cy="5" r="5" fill="currentColor"/>
      <path d="M2.6 5h4M5 3l2 2-2 2" stroke="#fff" stroke-width="1.3" fill="none" stroke-linecap="round" stroke-linejoin="round"/>
    </symbol>
    <symbol id="bullet-light" viewBox="0 0 10 10">
      <circle cx="5" cy="5" r="5" fill="#fff"/>
      <path d="M2.6 5h4M5 3l2 2-2 2" stroke="#4f2448" stroke-width="1.3" fill="none" stroke-linecap="round" stroke-linejoin="round"/>
    </symbol>
  </defs>
</svg>

<main class="board">

  <section class="post post-solution">
    <div class="photo" role="img" aria-label="Customer before and after photos, woman with long braids"></div>
    <svg class="wave" viewBox="0 0 379 189" preserveAspectRatio="none">
      <path d="M0 44 C60 0 180 0 270 50 C310 68 350 60 379 45 L379 189 L0 189 Z" fill="#26307a"/>
      <path d="M0 52 C60 10 180 12 270 60 C310 78 350 70 379 54 L379 189 L0 189 Z" fill="#ffffff"/>
    </svg>
    <p class="eyebrow">Burn belly fat fast:</p>
    <h2 class="headline">The 3-part solution<br>you need now!</h2>
    <ul class="benefits">
      <li><svg><use href="#bullet"/></svg>Melt stubborn belly fat</li>
      <li><svg><use href="#bullet"/></svg>Reduce bloating and inflammation</li>
      <li><svg><use href="#bullet"/></svg>Get that waistline snatched</li>
      <li><svg><use href="#bullet"/></svg>Boost energy and confidence</li>
    </ul>
    <div class="bottles" role="img" aria-label="Golden Meadow Kit, three supplement bottles"></div>
  </section>

  <section class="post post-struggle">
    <div class="photo" role="img" aria-label="Woman in white sportswear measuring her waist with a tape"></div>
    <div class="tag">STRUGGLING TO LOSE WEIGHT?</div>
    <h2 class="headline">Discover our ultimate solution!</h2>
    <div class="frame"></div>
    <ul class="benefits">
      <li><svg><use href="#bullet"/></svg>Melt stubborn belly fat</li>
      <li><svg><use href="#bullet"/></svg>Reduce bloating and inflammation</li>
      <li><svg><use href="#bullet"/></svg>Get that waistline snatched</li>
      <li><svg><use href="#bullet"/></svg>Boost energy and confidence</li>
    </ul>
  </section>

  <section class="post post-natural">
    <p class="eyebrow">Lose weight naturally:</p>
    <h2 class="headline">Ditch the prescription pills &amp;<br>needles!</h2>
    <div class="panel"></div>
    <div class="photo" role="img" aria-label="Smiling woman in a kitchen with the three bottles on the counter"></div>
    <div class="icon" style="top:155px"></div>
    <p class="icon-label" style="top:184px">Melt stubborn<br>belly fat</p>
    <div class="icon" style="top:214px"></div>
    <p class="icon-label" style="top:244px">Reduce bloating and<br>inflammation</p>
    <div class="icon" style="top:268px"></div>
    <p class="icon-label" style="top:298px">Get that waistline<br>snatched</p>
    <div class="icon" style="top:322px"></div>
    <p class="icon-label" style="top:352px">Boost energy and<br>confidence</p>
  </section>

  <section class="post post-beforeafter">
    <svg class="swoosh" viewBox="0 0 379 79" preserveAspectRatio="none">
      <path d="M0 30 C120 70 260 70 379 10 L379 79 L0 79 Z" fill="#2a5fe0" opacity=".45"/>
    </svg>
    <h2 class="headline">Melt away belly fat<br>faster with this powerful<br>trio!</h2>
    <div class="photo before" role="img" aria-label="Customer before photo, woman in black outfit"></div>
    <div class="photo after" role="img" aria-label="Customer after photo, woman in purple tie-dye top"></div>
    <p class="caption cap-before">Before</p>
    <p class="caption cap-after">After</p>
  </section>

  <section class="post post-double">
    <svg class="base" viewBox="0 0 379 379">
      <path d="M0 222 C80 200 140 250 230 270 C300 285 350 250 379 225 L379 379 L0 379 Z" fill="#4f2448"/>
      <path d="M210 268 C280 282 340 262 379 226 L379 232 C342 268 282 290 210 272 Z" fill="#c27bad"/>
    </svg>
    <div class="photo" role="img" aria-label="Smiling athletic woman holding an apple and a bathroom scale"></div>
    <h2 class="headline">Double your<br>weight loss<br>with this<br>powerful trio!</h2>
    <div class="bottles" role="img" aria-label="Golden Meadow Kit, three supplement bottles"></div>
    <ul class="benefits">
      <li><svg><use href="#bullet-light"/></svg>Melt stubborn belly fat</li>
      <li><svg><use href="#bullet-light"/></svg>Reduce bloating and inflammation</li>
      <li><svg><use href="#bullet-light"/></svg>Get that waistline snatched</li>
      <li><svg><use href="#bullet-light"/></svg>Boost energy and confidence</li>
    </ul>
  </section>

  <section class="post post-discover">
    <div class="photo" role="img" aria-label="Woman in pink activewear holding her waist"></div>
    <p class="eyebrow">Tired of stubborn belly fat?</p>
    <h2 class="headline">Discover the<br>trio that<br>works!</h2>
    <div class="snap snap-before" role="img" aria-label="Customer before photo"></div>
    <div class="snap snap-after" role="img" aria-label="Customer after photo"></div>
    <div class="bottles" role="img" aria-label="Golden Meadow Kit, three supplement bottles"></div>
    <div class="icon" style="left:188px;top:286px"></div>
    <p class="icon-label" style="left:165px;top:313px;width:70px">Melt stubborn<br>belly fat</p>
    <div class="icon" style="left:251px;top:285px"></div>
    <p class="icon-label" style="left:222px;top:314px;width:82px">Reduce bloating and<br>inflammation</p>
    <div class="icon" style="left:320px;top:283px"></div>
    <p class="icon-label" style="left:292px;top:312px;width:80px">Get that waistline<br>snatched</p>
    <div class="icon" style="left:183px;top:335px"></div>
    <p class="icon-label" style="left:210px;top:340px;text-align:left">Boost energy and<br>confidence</p>
  </section>

</main>
</body>
</html>
```